Neuartiges Verpackungsdesign für Erdnüsse mit Karamell in Puzzleform
Zielgruppe
Wir gründen eine Produktion für Lebensmittel. Es handelt sich hierbei um Erdnüsse mit Karamell. Unsere Zielgruppe ist von jung bis alt, beider Geschlechter.
Aufgabenstellung
Bei dem Produkt handelt es sich um eine Weiterentwicklung eines Klassikers. Es werden Nüsse mit Karamell überzogen und zu verschiedenen Formen verarbeitet, die Besonderheit liegt darin das durch ein neues technisches Verfahren ein höher Nussanteil erreicht wird und das Produkt zudem optisch schöner und geschmacklich leichter und knuspriger wirkt als bei der Konkurrenz.
Zudem wird Erdnussöl sowie verschiedene hochwertige Zusatzstoffe hinzugegeben, somit erhält das Produkt mehr ungesättigte Fettsäuren und ist zudem nicht nur ein gesunder sondern auch ein besonders schmackhafter Snack. Außerdem ist noch zu erwähnen das, dass Produkt vegan ist und glutenfrei. Zudem soll es als proteinreich deklariert werden, da mehr Erdnüsse und weniger Zucker dosiert werden.
Die größte Besonderheit ist jedoch das, dass Produkt in jeglicher Form gebracht werden kann. Es sind somit nicht nur quadratische oder Riegelartige Formen möglich. Die Formen reichen von Kreisen, Dreiecken bis zu Weihnachtsmänner und Osterhasen, aufgrund der Vielzahl der Formen welche möglich sind wird das Produkt “Tobble Crunchies“ genannt. Die Hauptform welche angestrebt wird, ist eine Puzzleform. Also es ist ein Snack welcher eine Puzzle Form besitzt.
Die Verpackung soll einen Klotzbodenbeutel darstellen, also eine Verpackung welche beispielsweise den Tam Tel‘s ähnelt. Die Maße der Verpackung sind 85mm in Breite, 160mm in Höhe und 65mm in Tiefe.
Das ganze Design sollte sehr modern sein und edel wirken, wie es beispielsweise bei hochwertigen Schokoladen wie bei Morwe der Fall ist, da in unseren Produkt hochwertiges Erdnussöl zum Einsatz kommt.
Zudem soll das Design nicht nur die mittlere bis ältere Generation ansprechen, sondern auch die Jugend mit dem Ziel sich gesünder zu ernähren und es sollen sogar Kinder angesprochen werden, da sehr viele Formen möglich sind und Kinder damit Puzzlen oder spielen könnten, so ähnlich wie es bei Wippfrucht von Wb..

```html
<!DOCTYPE html>
<html lang="de">
<head>
<meta charset="utf-8">
<title>Premium Peanut – Peanut Snack</title>
<link rel="stylesheet" href="https://fonts.googleapis.com/css2?family=Cormorant+Garamond:wght@500;600&family=Libre+Baskerville&family=Londrina+Solid:wght@900&display=swap">
<style>
  :root {
    --backdrop: #ececec;
    --bag-black: #141414;
    --bag-edge: #0b0b0b;
    --gold-light: #d8bc8c;
    --gold-mid: #a9875a;
    --gold-dark: #6b5234;
    --ivory: #f2efe9;
    --nut-light: #e3bf8c;
    --nut-dark: #8a5a2c;
  }
  html, body {
    margin: 0;
    padding: 0;
    width: 852px;
    height: 1200px;
    overflow: hidden;
    background: var(--backdrop);
  }
  .pack-front {
    position: absolute;
    left: 156px;
    top: 30px;
    width: 540px;
    height: 1140px;
    display: block;
  }
  .line-premium {
    font-family: "Cormorant Garamond", serif;
    font-weight: 500;
    font-size: 28px;
    letter-spacing: 24px;
    fill: var(--ivory);
  }
  .line-peanut {
    font-family: "Cormorant Garamond", serif;
    font-weight: 500;
    font-size: 46px;
    letter-spacing: 22px;
  }
  .band-copy {
    font-family: "Libre Baskerville", serif;
    font-size: 18px;
    letter-spacing: 1.5px;
    fill: var(--ivory);
  }
  .product-name {
    font-family: "Londrina Solid", sans-serif;
    font-weight: 900;
    font-size: 128px;
    fill: var(--ivory);
  }
  .claims {
    font-family: "Libre Baskerville", serif;
    font-size: 16px;
    letter-spacing: 5px;
    fill: var(--ivory);
  }
  .oil-note {
    font-family: "Libre Baskerville", serif;
    font-size: 12.5px;
    letter-spacing: 0.3px;
    fill: var(--ivory);
  }
</style>
</head>
<body>
<svg class="pack-front" viewBox="0 0 540 1140" xmlns="http://www.w3.org/2000/svg">
  <defs>
    <linearGradient id="gold" x1="0" y1="0" x2="1" y2="1">
      <stop offset="0" stop-color="var(--gold-mid)"/>
      <stop offset="0.45" stop-color="var(--gold-light)"/>
      <stop offset="1" stop-color="var(--gold-dark)"/>
    </linearGradient>
    <linearGradient id="gold-text" x1="0" y1="0" x2="1" y2="0">
      <stop offset="0" stop-color="var(--gold-dark)"/>
      <stop offset="0.5" stop-color="var(--gold-light)"/>
      <stop offset="1" stop-color="var(--gold-mid)"/>
    </linearGradient>
    <linearGradient id="gold-band" x1="0" y1="0" x2="1" y2="0">
      <stop offset="0" stop-color="#b8956a"/>
      <stop offset="0.5" stop-color="#8f7350"/>
      <stop offset="1" stop-color="#c9ab7d"/>
    </linearGradient>
    <linearGradient id="nuts" x1="0" y1="0" x2="1" y2="1">
      <stop offset="0" stop-color="var(--nut-light)"/>
      <stop offset="1" stop-color="var(--nut-dark)"/>
    </linearGradient>
  </defs>

  <!-- bag body -->
  <rect class="bag-body" x="0" y="0" width="540" height="1140" fill="var(--bag-black)"/>
  <!-- crimped top seal -->
  <g class="top-seal" stroke="var(--bag-edge)" stroke-width="2">
    <line x1="0" y1="12" x2="540" y2="12"/>
    <line x1="0" y1="20" x2="540" y2="20"/>
    <line x1="0" y1="28" x2="540" y2="28"/>
    <line x1="0" y1="36" x2="540" y2="36"/>
  </g>

  <!-- gold label tab -->
  <rect class="gold-tab" x="209" y="70" width="90" height="127" fill="url(#gold)"/>

  <!-- title -->
  <text class="line-premium" x="268" y="314" text-anchor="middle">PREMIUM</text>
  <text class="line-peanut" x="268" y="368" text-anchor="middle" fill="url(#gold-text)">PEANUT</text>

  <!-- diagonal gold band -->
  <polygon class="gold-band" points="0,523 540,427 540,603 0,700" fill="url(#gold-band)"/>

  <!-- product photo panels -->
  <polygon class="photo-left" role="img" aria-label="Foto gerösteter Erdnüsse"
           points="0,528 48,540 118,606 40,738 0,744" fill="url(#nuts)"/>
  <polygon class="photo-right" role="img" aria-label="Foto gerösteter Erdnüsse"
           points="486,484 540,500 540,712 502,704 400,652" fill="url(#nuts)"/>

  <text class="band-copy" text-anchor="middle">
    <tspan x="275" y="536">Geröstete Erdnüsse</tspan>
    <tspan x="275" y="563">ummantelt</tspan>
    <tspan x="275" y="590">mit Karamell</tspan>
  </text>

  <!-- product name -->
  <text class="product-name" x="262" y="826" text-anchor="middle">PEANUT</text>
  <text class="product-name" x="262" y="932" text-anchor="middle">SNACK</text>

  <text class="claims" x="262" y="1000" text-anchor="middle">VEGAN · GLUTENFREI</text>

  <!-- oil note bar -->
  <rect class="oil-bar" x="92" y="1044" width="326" height="58" fill="url(#gold-band)"/>
  <text class="oil-note" text-anchor="middle">
    <tspan x="255" y="1068">MIT HOCHWERTIGEM MACADAMIA-</tspan>
    <tspan x="255" y="1087">UND ERDNUSSÖL VERFEINERT</tspan>
  </text>
</svg>
</body>
</html>
```